New Toothpaste brand needs a logo & packaging design

Our company is launching a new toothpaste and is looking for a logo and packaging design. The toothpaste brand is called Brivana. The packaging should have the same design quality as the major international brands, such as Lumora, Lumora Totalcare, Dentiva, Pexolo, Wind-rise, Marvest, etc. The dominant colors for our brand should be hues of blue, similar to other major brands. In addition, there should be a little bit of green to represent the "Fresh Mint Blast" flavor and the "Extracts of Aloe Vera" included in the ingredients.

There are typically 3 unique sides on a toothpaste box:

The face: Repeated on ~3 sides of the 4 faces of the box
The back: The 4th box face has the instructions for use, ingredients, company information, bar code/product info, and some branding elements.
The sides: Usually consisting of just the logo, flavor etc.

Please refer to existing brands such as Lumora, Lumora Total-care, and Dentiva for an example of typical box layout and elements.

Task Details:
Package Dimensions: 180 mm x 48 mm x 28 mm, 100 ml toothpaste tube
Brand Name: Brivana
Description: Fluoride Toothpaste
Flavor: Fresh Mint Blast
5 Actions: Protects against cavities and tartar, freshens breath, whitens teeth, and maintains healthy gums. These actions can also be made into a list like Lumora Total Care or Dentiva Max care. For instance, Strong Teeth, Fresh Breath, Whitening, Healthy Gums, Cavity and Tartar Protection.
Also contains whitening micro particles and extracts of aloe vera which may be highlighted on the package

Overall, the look should be high quality and with the same look and feel as the big brands mentioned previously. We do not have an existing logo for this brand. The face of the package is the most important element as it is often repeated on several sides and on the tube itself.

Please let me know if you have any questions.

I've attached some of our favorite big brand designs below. I would say the Lumora Total Care and Gleam vers

The logos I've seen so far for Brivana, have been a bit too bold. A little bold is okay, but just needs to be moderate. 

I would like the colors to be bright and appealing. I mentioned shades of blue being the major color, but green should also be highlighted as well, perhaps in a 80% blue to 20% green ratio. 

Target Market(s)

adult consumer of toothpaste, both female and male.

Industry/Entity Type

It Company

Requirements
Must have
• A logo with the brand name: Brivana
Description or sub text: Fluoride Toothpaste
Flavor: Fresh Mint Blast
A phrase or list describing the Toothpaste Actions: e.g., Protects against cavities and tartar, freshens breath, whitens teeth, and maintains healthy gums. Or as a list simialr to Lumora Total Care or Dentiva Max Care:
-Anti-cavity
-Anti-tartar
-Fresh breath
-Whitening
-Healthy Gums

Special ingredient of "whitening micro particles: and "extracts of aloe vera", which should also be highlighted.

The color should mostly be shades of blue, with only a little bit of green to accentuate the fresh mint blast flavor and aloe vera

Nice to have
• The design should really look good next to lumora total care, gleam pure, and dentiva max care. These are our favorite designs.
Should not have
• For aloe vera, there is no need to show the plant.

The Brivana logo shouldn't be too Bold. This should be appeal to all consumers, not just men.

```html
<!DOCTYPE html>
<html lang="en">
<head>
<meta charset="utf-8">
<title>Brivana Fluoride Toothpaste – Logo and Box Face</title>
<link rel="stylesheet" href="https://fonts.googleapis.com/css2?family=Fira+Sans:ital,wght@0,600;0,700;0,800;1,700;1,800&display=swap">
<style>
  :root {
    --page-bg: #ffffff;
    --brand-blue: #2d3a9c;
    --panel-blue: #2a3690;
    --panel-blue-light: #3549b4;
    --panel-navy: #222a70;
    --edge-blue: #4fa6e6;
    --aloe-green: #3fae3a;
    --aloe-green-light: #a8ea8a;
    --aloe-text: #26388f;
    --mint-green: #5cae2e;
    --white: #ffffff;
  }
  * { box-sizing: border-box; margin: 0; padding: 0; }
  html, body {
    width: 1200px; height: 1000px; overflow: hidden;
    background: var(--page-bg);
    font-family: "Fira Sans", Arial, sans-serif;
  }
  .canvas { position: relative; width: 1200px; height: 1000px; }

  .brand-mark {
    position: absolute; left: 238px; top: 140px;
    font-size: 112px; font-weight: 800; line-height: 1;
    color: var(--brand-blue); letter-spacing: -2px;
  }

  .box-face {
    position: absolute; left: 205px; top: 650px;
    width: 810px; height: 218px; overflow: hidden;
  }
  .box-face svg { position: absolute; inset: 0; }
  .box-face .label { position: absolute; color: var(--white); white-space: nowrap; }

  .feature-line {
    font-size: 19px; font-weight: 800; font-style: italic;
    text-align: right; width: 300px; left: 50px;
  }
  .feature-line.first { top: 18px; }
  .feature-line.second { top: 46px; }

  .face-name {
    left: 36px; top: 72px;
    font-size: 74px; font-weight: 800; line-height: 1; letter-spacing: -1px;
  }
  .descriptor {
    left: 86px; top: 166px;
    font-size: 19px; font-weight: 700; letter-spacing: 0.3px;
  }

  .aloe-callout {
    left: 390px; width: 200px; text-align: center;
    color: var(--aloe-text) !important; font-style: italic; font-weight: 800;
  }
  .aloe-callout.small { top: 86px; font-size: 20px; }
  .aloe-callout.large { top: 110px; font-size: 26px; }

  .action-list {
    position: absolute; left: 652px; top: 29px; list-style: none;
    color: var(--white); font-size: 14px; font-weight: 600; letter-spacing: 0.6px;
  }
  .action-list li { height: 25.5px; display: flex; align-items: center; }
  .action-list svg { position: static; width: 10px; height: 10px; margin-right: 8px; }

  .flavor {
    right: 3px; top: 180px;
    font-size: 15px; font-weight: 800; font-style: italic; letter-spacing: 0.3px;
  }
</style>
</head>
<body>
<main class="canvas">
  <div class="brand-mark">Brivana</div>

  <section class="box-face" aria-label="Brivana toothpaste box face">
    <svg width="810" height="218" viewBox="0 0 810 218" aria-hidden="true">
      <defs>
        <linearGradient id="blue-panel" x1="0" y1="0" x2="1" y2="1">
          <stop offset="0" stop-color="var(--panel-blue)"/>
          <stop offset="0.6" stop-color="var(--panel-blue-light)"/>
          <stop offset="1" stop-color="var(--panel-blue)"/>
        </linearGradient>
        <radialGradient id="aloe-burst" cx="0.5" cy="0.55" r="0.6">
          <stop offset="0" stop-color="#ffffff"/>
          <stop offset="0.25" stop-color="var(--aloe-green-light)"/>
          <stop offset="1" stop-color="var(--aloe-green)"/>
        </radialGradient>
        <linearGradient id="mint-band" x1="0" y1="0" x2="1" y2="0">
          <stop offset="0" stop-color="var(--mint-green)" stop-opacity="0"/>
          <stop offset="0.35" stop-color="var(--mint-green)"/>
          <stop offset="1" stop-color="var(--mint-green)"/>
        </linearGradient>
      </defs>
      <rect class="panel-blue" width="810" height="218" fill="url(#blue-panel)"/>
      <rect class="panel-navy" x="600" width="210" height="218" fill="var(--panel-navy)"/>
      <path class="panel-aloe" d="M370 0 Q352 109 370 218 L620 218 Q600 109 610 0 Z" fill="url(#aloe-burst)"/>
      <path d="M370 0 Q352 109 370 218" fill="none" stroke="var(--edge-blue)" stroke-width="3"/>
      <path d="M610 0 Q600 109 620 218" fill="none" stroke="var(--edge-blue)" stroke-width="3"/>
      <rect class="mint-band" x="630" y="180" width="180" height="21" fill="url(#mint-band)"/>
    </svg>

    <span class="label feature-line first">WHITENING</span>
    <span class="label feature-line second">MICRO PARTICLES</span>
    <span class="label face-name">Brivana</span>
    <span class="label descriptor">FLUORIDE TOOTHPASTE</span>

    <span class="label aloe-callout small">EXTRACTS OF</span>
    <span class="label aloe-callout large">ALOE VERA</span>

    <ul class="action-list">
      <li><svg viewBox="0 0 10 10"><path d="M1 5.5 L4 8.5 L9 1.5" fill="none" stroke="#fff" stroke-width="1.6"/></svg>ANTI-CAVITY</li>
      <li><svg viewBox="0 0 10 10"><path d="M1 5.5 L4 8.5 L9 1.5" fill="none" stroke="#fff" stroke-width="1.6"/></svg>ANTI-TARTAR</li>
      <li><svg viewBox="0 0 10 10"><path d="M1 5.5 L4 8.5 L9 1.5" fill="none" stroke="#fff" stroke-width="1.6"/></svg>FRESH BREATH</li>
      <li><svg viewBox="0 0 10 10"><path d="M1 5.5 L4 8.5 L9 1.5" fill="none" stroke="#fff" stroke-width="1.6"/></svg>WHITENING</li>
      <li><svg viewBox="0 0 10 10"><path d="M1 5.5 L4 8.5 L9 1.5" fill="none" stroke="#fff" stroke-width="1.6"/></svg>HEALTHY GUMS</li>
    </ul>

    <span class="label flavor">FRESH MINT BLAST</span>
  </section>
</main>
</body>
</html>
```